依頼詳細
■依頼の目的/概要
2016年10月に大阪・梅田にオープンした緑陵学芸大学が運営するコワーキングスペース「MIDORI Ya HOSHI倶楽部ーミドリヤホシクラブー」。
本スペースを新たな居場所として、学生・卒業生・教職員だけでなく、たくさんの一般の方にもご利用いただいております。

しかし、「大学」が運営していることから、「図書館」のような静粛なイメージを持たれやすいのが悩みでした。
パンフレットのデザイン変更を機に、「初めてのコワーキングスペースは緑大!」とアピールできるくらい、親しみやすく、イキイキとしたイメージを広めたいと思っております。

■依頼詳細
「大学」の「コワーキングスペース」と聞くと、ハードルが高い、堅そうというイメージを持たれやすいですが、実際は、明るいコミュニティマネージャーのもと、親しみやすく居心地のよい空間を提供しています。

仕事帰りや合間に気軽に立ち寄ることができる立地で、ひとり時間が少しだけ贅沢になる空間づくりや、スタッフと会員の方とでつくる「まちかど研究室」など、会員同士が自然な形で新たなつながりが生まれる仕掛けも人気です。

大学運営なので価格も安く、高い志や目的がなくても、
「なんとなく生活している」
「少しだけ変化が欲しい」
と日常にちょっとだけもやもやしている方々に、ぜひ入会してほしいと思っております!

ターゲット:
便利な場所に仕事や学習のための環境がほしい人
職場や自宅以外に、なんとなく居場所がほしい人
コワーキングスペースを活用したことのない人

“大学っぽさ”をなくし、あらゆる大人たちが気軽に集え、気づきやちょっとした刺激が得られる場所と思われるようなデザインをお願いします!

■入れていただきたいワード
施設名:MIDOR Ya HOSHI倶楽部ーミドリヤホシクラブー
→パンフレットのデザインによっては、カタカナや平仮名、ローマ字で表現していただいてもOKです。
施設説明:会員制異業種交流サロン
キャッチコピー:あなたの新たな「居場所」

■仕様
・A4
・中綴じ
・デザイン箇所は表1(オモテ表紙)のみ

■重視する点
出来れば、過去・現在までにデザインの経験のある方を希望致します。

★ご参考★
公式HP
https://midori-yahoshi.jp/hoshiclub/
現在のパンフレット表紙や中身については添付画像をご確認ください。

その他何かご不明な点がございましたら、お気軽にご質問下さい。
よろしくお願いいたします。
サイズ
A4
ページ数
4ページ
希望イメージ
シンプル 複雑
単色 カラフル
暗い 明るい
日常 高級
遊び心 厳粛
未来的 伝統的
女性的 男性的
希望する色
赤系、黄・オレンジ系、茶系
納品ファイル
• 高解像度JPG (.jpg)
• イラストレーター形式 (.ai)
補足説明
パンフレットの表紙デザインのみの依頼です。
表紙以外については、パンフレットの色合いやイメージに合わせて、こちらで修正いたします。
依頼金額をUPいたしました。
現在の表紙デザイン(イラスト)は2023年3月までしか使えない契約となっております。
デザインは0から作成いただきますようお願いいたします。

この度は素敵なデザインをご提案くださりありがとうございました。
表紙に選ばせていただいた tomo7131のデザインは、目を引く色使いと我々が目指したい空間を上手に表現してくださっていたことが決め手でした。
次点のデザインも、表紙だけで「ワクワク」させられたり、本スペースの特徴を上手に表現してくださっていた点がとても魅力的でした。
表紙のデザインに負けないように、本スペースを盛り上げていかなくては、、と改めて決意した次第です。

この度は、短い期間での依頼にも関わらず、多くのご提案をしてくださりありがとうござました。
魅力的なデザインが多く、職場内でも意見が割れ、選定までに予想以上に時間がかかってしまいました。
選定の過程においても、みなさまのデザインの理由等にとても感動し、たくさんの気付きもありました。
お時間を割いていただきましたこと、改めてお礼申し上げます。

また機会がございましたら、ぜひよろしくお願いいたします!
本当にありがとうございました。

```html
<!DOCTYPE html>
<html lang="ja">
<head>
<meta charset="utf-8">
<title>MIDORI Ya HOSHI倶楽部 パンフレット表紙</title>
<link rel="stylesheet" href="https://fonts.googleapis.com/css2?family=M+PLUS+Rounded+1c:wght@500;800&family=Noto+Sans+JP:wght@500;700&display=swap">
<style>
  :root{
    --purple:#5a2d91;
    --violet:#8a3aa8;
    --magenta:#d8338c;
    --orange:#f28a1e;
    --yellow:#f8c51c;
    --grey:#d9dce3;
    --ink:#222226;
    --paper:#ffffff;
  }
  *{margin:0;padding:0;box-sizing:border-box}
  html,body{width:846px;height:1200px;overflow:hidden;background:var(--paper)}
  .cover{position:relative;width:846px;height:1200px;overflow:hidden;background:var(--paper);font-family:"Noto Sans JP",sans-serif;color:var(--ink)}
  .shapes{position:absolute;inset:0}
  .catch{position:absolute;top:345px;left:0;width:846px;text-align:center;font-family:"Noto Sans JP",sans-serif;font-weight:700;font-size:34px;line-height:1.4;letter-spacing:.06em}
  .title{position:absolute;top:458px;left:0;width:846px;text-align:center;font-family:"M PLUS Rounded 1c",sans-serif;font-weight:800;font-size:88px;line-height:1.05;letter-spacing:.12em;
    background:linear-gradient(90deg,var(--violet),var(--magenta) 50%,var(--orange));-webkit-background-clip:text;background-clip:text;color:transparent}
  .subtitle{position:absolute;top:658px;left:150px;width:546px;height:30px;background:var(--magenta);color:#fff;display:flex;align-items:center;justify-content:space-between;padding:0 16px;font-size:11px;font-weight:500}
  .subtitle strong{font-size:19px;font-weight:700;letter-spacing:.12em}
  .tag{position:absolute;font-size:13px;font-weight:700;white-space:nowrap;transform-origin:left center}
  .tag--light{color:#fff}
</style>
</head>
<body>
<main class="cover">
  <svg class="shapes" width="846" height="1200" viewBox="0 0 846 1200" aria-hidden="false">
    <defs>
      <linearGradient id="g-sunset" x1="0" y1="0" x2="1" y2="1">
        <stop offset="0" stop-color="#f8c51c"/><stop offset="1" stop-color="#d8338c"/>
      </linearGradient>
      <linearGradient id="g-dusk" x1="0" y1="0" x2="1" y2="1">
        <stop offset="0" stop-color="#d8338c"/><stop offset="1" stop-color="#5a2d91"/>
      </linearGradient>
      <linearGradient id="g-mist" x1="0" y1="0" x2="1" y2="1">
        <stop offset="0" stop-color="#ffffff"/><stop offset="1" stop-color="#cfd2da"/>
      </linearGradient>
      <linearGradient id="g-sun" x1="0" y1="0" x2="0" y2="1">
        <stop offset="0" stop-color="#f8c51c"/><stop offset="1" stop-color="#f28a1e"/>
      </linearGradient>
    </defs>
    <!-- background diamonds -->
    <rect x="470" y="-120" width="420" height="420" rx="30" transform="rotate(45 680 90)" fill="url(#g-mist)"/>
    <rect x="120" y="130" width="380" height="380" rx="30" transform="rotate(45 310 320)" fill="url(#g-mist)" opacity=".7"/>
    <rect x="470" y="520" width="360" height="360" rx="30" transform="rotate(45 650 700)" fill="url(#g-sunset)"/>
    <rect x="560" y="880" width="300" height="300" rx="26" transform="rotate(45 710 1030)" fill="url(#g-mist)"/>
    <rect x="-160" y="880" width="400" height="400" rx="30" transform="rotate(45 40 1080)" fill="url(#g-dusk)"/>
    <rect x="240" y="760" width="260" height="260" rx="24" transform="rotate(45 370 890)" fill="url(#g-mist)" opacity=".8"/>
    <!-- circles -->
    <circle cx="130" cy="175" r="150" fill="url(#g-sun)"/>
    <circle cx="50" cy="60" r="22" fill="#d8338c"/>
    <path d="M600 0 A120 120 0 0 0 846 0 Z" fill="#f8c51c"/>
    <path d="M640 0 A85 85 0 0 0 810 0 Z" fill="#8a3aa8"/>
    <circle cx="800" cy="560" r="70" fill="url(#g-sun)"/>
    <circle cx="245" cy="230" r="10" fill="#f28a1e"/>
    <circle cx="770" cy="1120" r="48" fill="#f8c51c"/>
    <circle cx="70" cy="820" r="14" fill="#d8338c"/>
    <circle cx="560" cy="1150" r="10" fill="#f28a1e"/>
    <circle cx="830" cy="270" r="12" fill="#d8338c"/>
    <!-- small figure illustrations -->
    <g role="img" aria-label="交流する人々の小さなイラスト" fill="#8a3aa8" opacity=".55">
      <rect x="150" y="320" width="12" height="34" rx="6"/>
      <rect x="520" y="150" width="12" height="34" rx="6"/>
      <rect x="700" y="320" width="12" height="34" rx="6"/>
      <rect x="740" y="420" width="12" height="34" rx="6"/>
      <rect x="90" y="740" width="12" height="34" rx="6"/>
      <rect x="210" y="880" width="12" height="34" rx="6"/>
      <rect x="430" y="780" width="12" height="34" rx="6"/>
      <rect x="520" y="930" width="12" height="34" rx="6"/>
      <rect x="660" y="960" width="12" height="34" rx="6"/>
      <rect x="380" y="1120" width="12" height="34" rx="6"/>
      <rect x="60" y="1120" width="12" height="34" rx="6"/>
      <rect x="300" y="620" width="12" height="34" rx="6"/>
    </g>
  </svg>

  <span class="tag tag--light" style="left:50px;top:205px;transform:rotate(-45deg)">ひとり時間を少しだけ贅沢に</span>
  <span class="tag" style="left:640px;top:120px;transform:rotate(-45deg)">ステキな出会いがある</span>
  <span class="tag" style="left:712px;top:940px;transform:rotate(-45deg)">まちかど研究室</span>
  <span class="tag tag--light" style="left:60px;top:1140px;transform:rotate(-45deg)">初めてのコワーキングスペースは緑大!</span>

  <p class="catch">あなたの<br>新たな「居場所」</p>
  <h1 class="title">ミドリヤ<br>ホシクラブ</h1>
  <div class="subtitle"><span>MIDORI Ya HOSHI</span><strong>会員制異業種交流サロン</strong><span>緑陵学芸大学</span></div>
</main>
</body>
</html>
```